Young, modern, highly skilled carpenter needs business card design

I need a business card design for my construction business. Its called 'Pellwright Construction Solutions'. Im looking for a ultra modern design that incorporates P C S, the first letters of the name with only a subtle reference to carpentry. The design should reflect my high quality work and eye for detail. i have also uploaded some exmaple designs i like.

Industry/Entity Type

Construction

Requirements
Must have
• Name of business, my name, mobile number, ABN number, email address
Nice to have
• A logo incorporating the name of the business

```html
<!DOCTYPE html>
<html lang="en">
<head>
<meta charset="utf-8">
<title>Pellwright Construction Solutions – Business Card</title>
<link rel="stylesheet" href="https://fonts.googleapis.com/css2?family=Ubuntu:wght@500;700&family=Ubuntu+Mono&display=swap">
<style>
  :root {
    --backdrop: #2b2820;
    --wood-light: #f0d2ab;
    --wood-mid: #e2b888;
    --wood-deep: #d19e6c;
    --ink: #3a2a1e;
    --ink-soft: #4a3828;
  }
  * { box-sizing: border-box; margin: 0; padding: 0; }
  html, body {
    width: 1200px;
    height: 900px;
    overflow: hidden;
    background: var(--backdrop);
  }
  .stage {
    width: 1200px;
    height: 900px;
    display: flex;
    align-items: center;
    justify-content: center;
  }
  .business-card {
    position: relative;
    width: 900px;
    height: 520px;
    overflow: hidden;
    border-radius: 4px;
    color: var(--ink);
  }
  .wood-surface {
    position: absolute;
    inset: 0;
    background:
      linear-gradient(178deg, transparent 0 18%, rgba(209,158,108,.35) 22%, transparent 28% 52%, rgba(209,158,108,.3) 58%, transparent 64% 80%, rgba(209,158,108,.35) 86%, transparent 92%),
      linear-gradient(180deg, var(--wood-light) 0%, var(--wood-mid) 45%, var(--wood-light) 70%, var(--wood-mid) 100%);
  }
  .card-content {
    position: relative;
    width: 100%;
    height: 100%;
  }
  .brand-mark {
    position: absolute;
    top: 48px;
    left: 0;
    width: 100%;
    text-align: center;
    font-family: "Ubuntu", sans-serif;
    font-weight: 700;
    font-size: 68px;
    letter-spacing: 6px;
    line-height: 1;
  }
  .company-name {
    position: absolute;
    top: 132px;
    left: 0;
    width: 100%;
    text-align: center;
    font-family: "Ubuntu", sans-serif;
    font-weight: 700;
    font-size: 28px;
  }
  .person-name {
    position: absolute;
    top: 196px;
    left: 0;
    width: 100%;
    text-align: center;
    font-family: "Ubuntu", sans-serif;
    font-weight: 700;
    font-size: 42px;
  }
  .person-role {
    position: absolute;
    top: 250px;
    left: 0;
    width: 100%;
    text-align: center;
    font-family: "Ubuntu", sans-serif;
    font-weight: 500;
    font-size: 21px;
    color: var(--ink-soft);
  }
  .contact {
    position: absolute;
    font-family: "Ubuntu Mono", monospace;
    font-size: 25px;
    color: var(--ink-soft);
    letter-spacing: 1px;
  }
  .contact-address { left: 60px; top: 320px; }
  .contact-email { left: 60px; top: 370px; }
  .contact-phone { right: 60px; top: 400px; font-size: 28px; }
  .contact-abn { right: 60px; top: 448px; font-size: 28px; }
</style>
</head>
<body>
  <main class="stage">
    <article class="business-card">
      <div class="wood-surface" role="img" aria-label="Light oak wood grain texture across the card face"></div>
      <div class="card-content">
        <div class="brand-mark">PCS</div>
        <div class="company-name">Pellwright Construction Solutions</div>
        <div class="person-name">Your Name</div>
        <div class="person-role">carpenter</div>
        <div class="contact contact-address">18 Kowhai Ridge Lane, Tauranga</div>
        <div class="contact contact-email">info@PellwrightConstruction.nz</div>
        <div class="contact contact-phone">(07) 555 0142</div>
        <div class="contact contact-abn">ABN: 98 765 432 100</div>
      </div>
    </article>
  </main>
</body>
</html>
```